Qualified Machining Operator Training Program

We need a flyer to advertise a training program to business. I will attach a rough draft "original file" that we need enhanced to look professional. Details to the program are here https://www.halvornskills.org/credentials/machining-credential-qmo/ We want it to look clean and professional.

Please use the information that is on the "original file" rough draft. I have attached an example pdf, the reason I don't like the example is because it has too many words and looks out of date.

Font styles to use
Serif
Sans Serif

```html
<!DOCTYPE html>
<html lang="en">
<head>
<meta charset="utf-8">
<title>Qualified Machining Operator Program Flyer</title>
<link href="https://fonts.googleapis.com/css2?family=Open+Sans:wght@400;600;700;800&family=Questrial&display=swap" rel="stylesheet">
<style>
  :root {
    --navy: #1c2f6e;
    --navy-deep: #141d5c;
    --ink: #2d2d2d;
    --charcoal: #333335;
    --gray-title: #4a4a4a;
    --white: #ffffff;
    --page-bg: #f2f2f2;
  }
  * { margin: 0; padding: 0; box-sizing: border-box; }
  html, body { width: 1200px; height: 1200px; overflow: hidden; background: var(--page-bg); }
  .flyer {
    position: absolute; left: 172px; top: 0; width: 856px; height: 1200px;
    background: var(--white); overflow: hidden;
    font-family: "Questrial", sans-serif; color: var(--ink);
  }
  .abs { position: absolute; }

  /* header */
  .header-band { left: 0; top: 0; width: 856px; height: 138px; }
  .brand { left: 42px; top: 56px; display: flex; align-items: center; gap: 10px; }
  .brand-dot { width: 26px; height: 26px; border-radius: 50%; background: var(--navy); }
  .brand-name { font-family: "Open Sans", sans-serif; font-weight: 700; font-size: 26px; color: var(--navy); letter-spacing: 1px; }
  .contact { top: 35px; font-size: 24px; color: var(--white); display: flex; align-items: center; gap: 8px; }
  .contact.phone { left: 312px; font-weight: 700; }
  .contact.email { left: 558px; font-size: 21px; }
  .onsite { left: 339px; top: 72px; font-size: 38px; font-weight: 700; color: var(--white); -webkit-text-stroke: 0.6px var(--white); }

  /* hero */
  .hero-photo { left: 0; top: 138px; width: 856px; height: 443px;
    background: linear-gradient(100deg, #8c8a86 0%, #a9a7a2 30%, #b6bcc6 48%, #dde3ee 62%, #eef1f7 75%, #e4eaf4 100%); }
  .title { right: 88px; text-align: right; font-family: "Open Sans", sans-serif; line-height: 1; }
  .title.light { font-weight: 400; color: var(--gray-title); font-size: 60px; }
  .title.bold { font-weight: 800; color: var(--navy-deep); font-size: 54px; }
  .t1 { top: 200px; } .t2 { top: 274px; } .t3 { top: 334px; } .t4 { top: 395px; color: var(--ink); }

  /* skills */
  .skills-shape { left: 0; top: 524px; width: 856px; height: 174px; }
  .skills-heading { left: 0; width: 856px; top: 545px; font-family: "Open Sans", sans-serif;
    font-weight: 700; font-size: 36px; color: var(--white); letter-spacing: 1px; display: flex; justify-content: center; align-items: center; gap: 18px; }
  .skills-heading .rule { width: 52px; height: 2px; background: var(--white); }
  .skill-col { top: 601px; list-style: none; color: var(--white); font-size: 14.5px; line-height: 17px; }
  .skill-col li { position: relative; padding-left: 15px; margin-bottom: 12px; }
  .skill-col li::before { content: ""; position: absolute; left: 0; top: 6px; width: 6px; height: 6px; border-radius: 50%; background: var(--white); }

  /* focus chevrons */
  .focus-bar { left: 47px; top: 718px; width: 761px; height: 98px; }
  .focus-label { top: 718px; height: 98px; display: flex; align-items: center; justify-content: center; text-align: center;
    font-family: "Open Sans", sans-serif; font-weight: 700; color: var(--white); font-size: 20px; line-height: 1.25; }
  .focus-label.wide { font-size: 18px; justify-content: flex-end; text-align: right; }

  /* feature box */
  .feature-box { left: 47px; top: 835px; width: 761px; height: 173px; background: var(--charcoal); }
  .screen-area { left: 56px; top: 845px; width: 254px; height: 155px; background: linear-gradient(135deg, #f4f6f8, #dfe7ea); }
  .trainer-area { left: 544px; top: 845px; width: 254px; height: 155px; background: var(--white); }
  .trainer-img { left: 554px; top: 855px; width: 125px; height: 135px; background: linear-gradient(160deg, #3c6fc0 0%, #9aa3ad 55%, #c7ccd2 100%); border-radius: 4px; }
  .hours { right: 66px; top: 938px; text-align: right; color: var(--ink); }
  .hours .big { font-family: "Open Sans", sans-serif; font-weight: 700; font-size: 21px; line-height: 1.1; }
  .hours .small { font-family: "Open Sans", sans-serif; font-weight: 600; font-size: 11px; line-height: 1.3; }
  .hours .small.thin { font-family: "Questrial", sans-serif; font-weight: 400; }
  .feature-list { left: 310px; width: 234px; top: 878px; text-align: center; color: var(--white); font-weight: 700; font-size: 16px; line-height: 31px; }

  /* quote */
  .quote { left: 75px; width: 690px; top: 1040px; font-size: 11.8px; font-weight: 700; line-height: 15px; text-align: justify; color: var(--ink); }
  .qmark { font-family: "Open Sans", sans-serif; font-weight: 800; font-size: 40px; color: var(--navy-deep); line-height: 1; }
  .q-open { left: 46px; top: 1020px; } .q-close { left: 786px; top: 1062px; }

  /* partners */
  .partner { top: 1120px; display: flex; align-items: center; height: 40px; font-family: "Open Sans", sans-serif; font-weight: 700; font-size: 22px; color: var(--navy-deep); }
  .partner.red { color: #d5121b; }
  .badge { top: 1112px; }

  .footer-band { left: 0; top: 1166px; width: 856px; height: 34px; }
</style>
</head>
<body>
<div class="flyer">

  <svg class="abs header-band" viewBox="0 0 856 138" aria-hidden="true">
    <defs>
      <linearGradient id="hdr" x1="0" x2="1" y1="0" y2="0">
        <stop offset="0" stop-color="#2b2b2c"/><stop offset="1" stop-color="#3b3b3d"/>
      </linearGradient>
    </defs>
    <rect width="856" height="138" fill="url(#hdr)"/>
    <polygon points="0,0 210,0 265,138 0,138" fill="#ffffff"/>
  </svg>

  <div class="abs brand"><span class="brand-dot"></span><span class="brand-name">HALVORN</span></div>

  <div class="abs contact phone">
    <svg width="20" height="20" viewBox="0 0 24 24" aria-hidden="true"><path d="M6.6 10.8c1.4 2.8 3.8 5.1 6.6 6.6l2.2-2.2c.3-.3.7-.4 1-.2 1.1.4 2.3.6 3.6.6.6 0 1 .4 1 1V20c0 .6-.4 1-1 1C10.6 21 3 13.4 3 4c0-.6.4-1 1-1h3.5c.6 0 1 .4 1 1 0 1.3.2 2.5.6 3.6.1.3 0 .7-.2 1L6.6 10.8z" fill="#fff"/></svg>
    <span>555 014 2290</span>
  </div>
  <div class="abs contact email">
    <svg width="22" height="16" viewBox="0 0 22 16" aria-hidden="true"><rect x="0" y="0" width="22" height="16" rx="1.5" fill="#fff"/><polyline points="1,1.5 11,9 21,1.5" fill="none" stroke="#333335" stroke-width="2"/></svg>
    <span>dana@northpeaklean.com</span>
  </div>
  <div class="abs onsite">On-site training available</div>

  <div class="abs hero-photo" role="img" aria-label="Photo of a hands-on machining trainer bench with a blue electric motor, pneumatic parts and yellow tubing, fading into a light blue backdrop"></div>

  <div class="abs title light t1">Qualified</div>
  <div class="abs title bold t2">MACHINING</div>
  <div class="abs title bold t3">OPERATOR</div>
  <div class="abs title light t4">Program</div>

  <svg class="abs skills-shape" viewBox="0 0 856 174" aria-hidden="true">
    <polygon points="130,57 188,2 651,2 704,57" fill="#9aa0ab"/>
    <polygon points="128,57 188,0 652,0 706,57" fill="#1c2f6e"/>
    <rect x="0" y="57" width="856" height="117" fill="#1c2f6e"/>
  </svg>
  <div class="abs skills-heading"><span class="rule"></span>SKILLS TAUGHT<span class="rule"></span></div>

  <ul class="abs skill-col" style="left:47px">
    <li>Communication</li><li>Lean Principles</li><li>Problem Solving</li>
  </ul>
  <ul class="abs skill-col" style="left:213px">
    <li>Total Productive<br>Maintenance</li><li>Project<br>Management</li>
  </ul>
  <ul class="abs skill-col" style="left:369px">
    <li>Locating<br>Information</li><li>Supply Chain &amp;<br>Logistics</li>
  </ul>
  <ul class="abs skill-col" style="left:520px">
    <li>Autonomous<br>Maintenance</li><li>Total Productive<br>Maintenance</li>
  </ul>
  <ul class="abs skill-col" style="left:676px">
    <li>Data Analysis</li><li>Customer Service</li><li>Teamwork</li>
  </ul>

  <svg class="abs focus-bar" viewBox="0 0 761 98" role="img" aria-label="Four chevron panels with dark workshop photos: safety, quality, processes, maintenance awareness">
    <polygon points="0,0 190,0 210,49 190,98 0,98" fill="#3a3026"/>
    <polygon points="196,0 385,0 405,49 385,98 196,98 216,49" fill="#2f3033"/>
    <polygon points="391,0 580,0 600,49 580,98 391,98 411,49" fill="#34302c"/>
    <polygon points="586,0 761,0 761,98 586,98 606,49" fill="#2a2c30"/>
  </svg>
  <div class="abs focus-label" style="left:47px;width:190px">SAFETY</div>
  <div class="abs focus-label" style="left:250px;width:180px">QUALITY</div>
  <div class="abs focus-label" style="left:445px;width:180px">PROCESSES</div>
  <div class="abs focus-label wide" style="left:658px;width:142px">MAINTENANCE<br>AWARENESS</div>

  <div class="abs feature-box"></div>
  <div class="abs screen-area" role="img" aria-label="Screenshot of interactive training software showing a pneumatic cylinder schematic"></div>
  <div class="abs feature-list">Advanced Manufacturing<br>Hands-On Learning<br>College Credits Eligible</div>
  <div class="abs trainer-area"></div>
  <div class="abs trainer-img" role="img" aria-label="Photo of a portable blue training cart with a clear-covered mechatronics bench"></div>
  <div class="abs hours">
    <div class="big">120 hours</div>
    <div class="small">$2,500 per student</div>
    <div class="small thin">ETP Reimbursement</div>
  </div>

  <div class="abs qmark q-open">&ldquo;</div>
  <p class="abs quote">we feel that Halvorn QMO certification compliments not only the qualifications of the candidates we see, but also enhances the knowledge, skills, and abilities of existing team members in our pursuit of manufacturing excellence</p>
  <div class="abs qmark q-close">&rdquo;</div>

  <div class="abs partner" style="left:47px">Corvell</div>
  <div class="abs partner red" style="left:220px">Makoro</div>
  <svg class="abs badge" style="left:420px" width="40" height="56" viewBox="0 0 40 56" aria-hidden="true"><rect x="4" y="2" width="32" height="32" fill="#1f7a45"/><rect x="8" y="40" width="24" height="3" fill="#9a9a9a"/><rect x="10" y="47" width="20" height="2" fill="#bbbbbb"/></svg>
  <svg class="abs badge" style="left:570px;top:1120px" width="56" height="36" viewBox="0 0 56 36" aria-hidden="true"><ellipse cx="28" cy="18" rx="27" ry="16" fill="#1c2f6e"/></svg>
  <svg class="abs badge" style="left:755px;top:1108px" width="52" height="52" viewBox="0 0 52 52" aria-hidden="true"><circle cx="26" cy="26" r="24" fill="#b4b8bf"/><circle cx="26" cy="26" r="15" fill="#1c2f6e"/></svg>

  <svg class="abs footer-band" viewBox="0 0 856 34" aria-hidden="true">
    <defs>
      <linearGradient id="ftr" x1="0" x2="1" y1="0" y2="0">
        <stop offset="0" stop-color="#5a5c60"/><stop offset="0.35" stop-color="#d8d9db"/><stop offset="0.6" stop-color="#6c6e72"/><stop offset="1" stop-color="#3d3f44"/>
      </linearGradient>
    </defs>
    <rect y="8" width="856" height="26" fill="url(#ftr)"/>
    <polygon points="0,0 420,0 450,34 0,34" fill="#1c2f6e"/>
  </svg>
</div>
</body>
</html>
```